Holistic Health Coach needs simple web site design for a new practice

I need a web (re)design for my entire site, TR Maple Sprout. I have a beautiful new blue and green logo that I'd like the site fonts and color scheme to be built around. I'll attach my new logo so you'll know the colors/design feel I'm after.

I want easy navigation for my mostly text based site, widgets for my social media pages and a clean, fun, light feel for the site.

Target Market(s)

People looking to take charge of their own health, and who may need my coaching services to obtain optimal wellness.

Industry/Entity Type

Health

Coding

Number of Pages Required

Font styles to use
Script

Colors
33b8a4
33a6d7
ffffff

Requirements
Must have
• Must incorporate my logo design, as well as same/similar fonts and color scheme.
• I'd like it to stay as close to the current design as possible.
Nice to have
• Would love to incorporate a hover over menu (for example, when a user hovers over "About", they will see the submenu in a floating design.
Should not have
• No dark colors or masculine feel

```html
<!DOCTYPE html>
<html lang="en">
<head>
<meta charset="utf-8">
<title>TR Maple Sprout – Holistic Health Coaching</title>
<link href="https://fonts.googleapis.com/css2?family=Open+Sans:wght@400;600&family=Roboto+Slab:wght@300;400&family=Sofia&display=swap" rel="stylesheet">
<style>
:root{
  --teal:#33b8a4;
  --teal-dark:#0f9a96;
  --teal-deeper:#0c9490;
  --blue:#33a6d7;
  --link:#1f8fc0;
  --green:#6cbf2a;
  --page:#f1f1f1;
  --white:#ffffff;
  --text:#444;
  --muted:#b0b0b0;
  --line:#e2e2e2;
  --footer:#0b4f5a;
  --footer-deep:#073b44;
  --banner-a:#2f8f12;
  --banner-b:#0b5d06;
}
*{box-sizing:border-box;margin:0;padding:0}
html,body{width:1200px;height:2639px;overflow:hidden}
body{background:var(--page);font-family:"Open Sans",sans-serif;color:var(--text);position:relative}
a{color:inherit;text-decoration:none}

.site-header{height:86px;background:var(--white);display:flex;align-items:center;padding:0 72px;justify-content:space-between}
.brand{font-family:"Sofia",cursive;font-size:32px;color:var(--teal)}
.main-nav{display:flex;gap:58px;font-size:16px;color:var(--link);margin-right:-10px}
.main-nav .current{color:var(--teal)}

.hero{height:280px;background:radial-gradient(ellipse at 55% 40%,#3fb51c 0%,var(--banner-a) 40%,var(--banner-b) 100%);position:relative}
.hero-portrait{position:absolute;left:86px;top:0;width:270px;height:280px;background:linear-gradient(180deg,#6f9c5a,#3f7a2e)}
.hero-text{position:absolute;left:400px;right:90px;top:60px;text-align:center;font-family:"Sofia",cursive;color:var(--white);font-size:33px;line-height:48px}

.layout{position:absolute;top:388px;left:73px;width:1054px;display:flex;justify-content:space-between}
.posts{width:728px}
.post{background:var(--white);border:1px solid var(--line);border-radius:4px;height:566px;display:flex;margin-bottom:32px;overflow:hidden}
.post-meta{width:162px;background:var(--teal-dark);color:var(--white);flex:none}
.post-date{text-align:center;font-family:"Roboto Slab",serif;padding:8px 0 14px;background:var(--teal-deeper);border-bottom:1px solid rgba(255,255,255,.25)}
.post-date .day{font-size:44px;line-height:50px}
.post-date .mon,.post-date .yr{font-size:24px;line-height:30px;font-weight:300}
.meta-row{display:flex;gap:12px;padding:14px 10px 12px;border-bottom:1px solid rgba(255,255,255,.25);font-size:11px;line-height:15px}
.meta-row svg{flex:none;margin-top:1px}
.meta-row b{display:block;font-weight:600;color:#bff3ec;letter-spacing:.3px}
.share{display:flex;flex-wrap:wrap;gap:6px;padding:10px 8px}
.share span{border:1px solid #fff;border-radius:2px;font-size:11px;padding:2px 6px}
.post-body{padding:20px 16px 0 16px;flex:1}
.post-title{font-family:"Roboto Slab",serif;font-weight:300;color:var(--blue);font-size:29px;line-height:34px;margin-bottom:14px;max-width:440px}
.post-body p{font-size:12.5px;line-height:18px}
.post-figure{width:425px;height:248px;margin:10px auto 14px;border:4px solid #dfe9ee;background:linear-gradient(135deg,#e8e8e8,#bfbfbf)}
.read-more{display:inline-block;margin-top:14px;background:var(--blue);color:#fff;font-size:13px;padding:10px 16px;border-radius:3px}
.pager{display:flex;gap:12px;margin-top:-2px}
.pager span{background:var(--blue);color:#fff;font-size:12px;padding:9px 16px;border-radius:3px}

.sidebar{width:307px}
.widget{background:var(--white);border:1px solid var(--line);border-radius:4px;padding:18px 14px;margin-bottom:22px}
.widget-title{font-family:"Sofia",cursive;font-weight:400;color:var(--teal);font-size:22px;text-align:center;white-space:nowrap}
.flourish{display:block;margin:8px auto 16px}
.recent li{list-style:none;font-size:12.5px;color:var(--muted);border-bottom:1px solid #eee;padding:10px 0;line-height:18px}
.comments li{list-style:none;font-size:12.5px;color:var(--link);display:flex;gap:10px;padding:12px 0;border-bottom:1px solid #eee;line-height:18px}
.comments li svg{flex:none;margin-top:3px}
.comments li b{color:#333}
.photo-grid{height:320px;background:linear-gradient(135deg,#b88f86,#3b3b5e 50%,#8aa6c7);margin:8px 8px 18px}
.insta-actions{display:flex;gap:8px;justify-content:center}
.insta-actions span{color:#fff;font-size:13px;padding:8px 12px;border-radius:3px}
.btn-teal{background:var(--teal)}
.btn-green{background:var(--green)}
.promo{height:268px;background:linear-gradient(160deg,#ffffff,#cfeef5 60%,#f7b24a)}

.site-footer{position:absolute;top:2260px;left:0;width:1200px;height:331px;background:var(--footer);color:#fff;padding:22px 78px 0;display:flex}
.f-col{width:355px}
.f-title{font-size:16px;font-weight:400;padding-bottom:12px;border-bottom:1px dashed rgba(255,255,255,.35);width:290px;margin-bottom:12px}
.f-list li{list-style:none;font-size:12px;display:flex;gap:14px;align-items:center;height:25px}
.f-text{font-size:12.5px;line-height:19px;width:300px}
.subscribe{display:flex;margin:14px 0 26px}
.subscribe span{width:228px;height:32px;background:#fff;color:#aaa;font-size:11px;padding:9px 12px}
.subscribe b{width:86px;background:var(--green);font-size:13px;font-weight:600;display:flex;align-items:center;justify-content:center}
.socials{display:flex;gap:12px}
.socials i{width:40px;height:40px;border-radius:50%;background:#6f7c80;display:block}
.footer-bar{position:absolute;top:2591px;left:0;width:1200px;height:48px;background:var(--footer-deep);color:#fff;font-size:12px;display:flex;align-items:center;justify-content:center}
.footer-bar span{color:var(--teal);margin-right:4px}
</style>
</head>
<body>

<header class="site-header">
  <div class="brand">TR Maple Sprout</div>
  <nav class="main-nav">
    <a class="current">About Dana</a>
    <a>Articles</a>
    <a>Essential Oil</a>
    <a>21-Day Sweet Reset Coaching Services</a>
  </nav>
</header>

<section class="hero">
  <div class="hero-portrait" role="img" aria-label="Portrait photo of the health coach"></div>
  <p class="hero-text">I am Dana, a certified V.I.T.A Holistic Life Coach Level 1, a Certified 21-Day Sweet Reset Coach</p>
</section>

<main class="layout">
  <div class="posts">
    <article class="post">
      <aside class="post-meta">
        <div class="post-date"><div class="day">12</div><div class="mon">Apr</div><div class="yr">2015</div></div>
        <div class="meta-row"><svg width="12" height="12" viewBox="0 0 12 12"><circle cx="6" cy="3.5" r="2.8" fill="#fff"/><path d="M1 12c0-4 10-4 10 0z" fill="#fff"/></svg><div><b>POSTED BY</b>ADMIN</div></div>
        <div class="meta-row"><svg width="12" height="14" viewBox="0 0 12 14"><path d="M1 0h7l3 3v11H1z" fill="#fff"/></svg><div><b>POSTED IN</b>Category 1,<br>Category 2,<br>Category 3</div></div>
        <div class="meta-row"><svg width="14" height="12" viewBox="0 0 14 12"><ellipse cx="7" cy="5" rx="7" ry="5" fill="#fff"/></svg><div><b>DISCUSSION</b>11 comments</div></div>
        <div class="meta-row"><svg width="12" height="12" viewBox="0 0 12 12"><circle cx="10" cy="2" r="2" fill="#fff"/><circle cx="2" cy="6" r="2" fill="#fff"/><circle cx="10" cy="10" r="2" fill="#fff"/><path d="M10 2L2 6l8 4" stroke="#fff" fill="none"/></svg><div><b>SHARE THIS</b></div></div>
        <div class="share"><span>Email</span><span>Print</span><span>Friendbook</span><span>Chirper</span><span>Circles</span><span>Pinboard</span></div>
      </aside>
      <div class="post-body">
        <h2 class="post-title">April Essential Living Education Series</h2>
        <p>During the month of April, I will be doing a series of Friendbook classes designed with you in mind. Topics range from skin care and personal care to Healing Oils of the Garden, Hormones, and how to have a Chemical Free Home.</p>
        <div class="post-figure" role="img" aria-label="Photo of large black typography lettering"></div>
        <p>I hope you can join me for some fun educational Friendbook classes!! Please let me know what other classes you'd like to see</p>
        <span class="read-more">Read More</span>
      </div>
    </article>

    <article class="post">
      <aside class="post-meta">
        <div class="post-date"><div class="day">12</div><div class="mon">Apr</div><div class="yr">2015</div></div>
        <div class="meta-row"><svg width="12" height="12" viewBox="0 0 12 12"><circle cx="6" cy="3.5" r="2.8" fill="#fff"/><path d="M1 12c0-4 10-4 10 0z" fill="#fff"/></svg><div><b>POSTED BY</b>ADMIN</div></div>
        <div class="meta-row"><svg width="12" height="14" viewBox="0 0 12 14"><path d="M1 0h7l3 3v11H1z" fill="#fff"/></svg><div><b>POSTED IN</b>Category 1,<br>Category 2,<br>Category 3</div></div>
        <div class="meta-row"><svg width="14" height="12" viewBox="0 0 14 12"><ellipse cx="7" cy="5" rx="7" ry="5" fill="#fff"/></svg><div><b>DISCUSSION</b>11 comments</div></div>
        <div class="meta-row"><svg width="12" height="12" viewBox="0 0 12 12"><circle cx="10" cy="2" r="2" fill="#fff"/><circle cx="2" cy="6" r="2" fill="#fff"/><circle cx="10" cy="10" r="2" fill="#fff"/><path d="M10 2L2 6l8 4" stroke="#fff" fill="none"/></svg><div><b>SHARE THIS</b></div></div>
        <div class="share"><span>Email</span><span>Print</span><span>Friendbook</span><span>Chirper</span><span>Circles</span><span>Pinboard</span></div>
      </aside>
      <div class="post-body">
        <h2 class="post-title">April Essential Living Education Series</h2>
        <p>During the month of April, I will be doing a series of Friendbook classes designed with you in mind. Topics range from skin care and personal care to Healing Oils of the Garden, Hormones, and how to have a Chemical Free Home.</p>
        <div class="post-figure" role="img" aria-label="Photo of large black typography lettering"></div>
        <p>I hope you can join me for some fun educational Friendbook classes!! Please let me know what other classes you'd like to see</p>
        <span class="read-more">Read More</span>
      </div>
    </article>

    <article class="post">
      <aside class="post-meta">
        <div class="post-date"><div class="day">12</div><div class="mon">Apr</div><div class="yr">2015</div></div>
        <div class="meta-row"><svg width="12" height="12" viewBox="0 0 12 12"><circle cx="6" cy="3.5" r="2.8" fill="#fff"/><path d="M1 12c0-4 10-4 10 0z" fill="#fff"/></svg><div><b>POSTED BY</b>ADMIN</div></div>
        <div class="meta-row"><svg width="12" height="14" viewBox="0 0 12 14"><path d="M1 0h7l3 3v11H1z" fill="#fff"/></svg><div><b>POSTED IN</b>Category 1,<br>Category 2,<br>Category 3</div></div>
        <div class="meta-row"><svg width="14" height="12" viewBox="0 0 14 12"><ellipse cx="7" cy="5" rx="7" ry="5" fill="#fff"/></svg><div><b>DISCUSSION</b>11 comments</div></div>
        <div class="meta-row"><svg width="12" height="12" viewBox="0 0 12 12"><circle cx="10" cy="2" r="2" fill="#fff"/><circle cx="2" cy="6" r="2" fill="#fff"/><circle cx="10" cy="10" r="2" fill="#fff"/><path d="M10 2L2 6l8 4" stroke="#fff" fill="none"/></svg><div><b>SHARE THIS</b></div></div>
        <div class="share"><span>Email</span><span>Print</span><span>Friendbook</span><span>Chirper</span><span>Circles</span><span>Pinboard</span></div>
      </aside>
      <div class="post-body">
        <h2 class="post-title">April Essential Living Education Series</h2>
        <p>During the month of April, I will be doing a series of Friendbook classes designed with you in mind. Topics range from skin care and personal care to Healing Oils of the Garden, Hormones, and how to have a Chemical Free Home.</p>
        <div class="post-figure" role="img" aria-label="Photo of large black typography lettering"></div>
        <p>I hope you can join me for some fun educational Friendbook classes!! Please let me know what other classes you'd like to see</p>
        <span class="read-more">Read More</span>
      </div>
    </article>

    <nav class="pager"><span>&#9664; Older Post</span><span>Newer Post &#9654;</span></nav>
  </div>

  <aside class="sidebar">
    <section class="widget" style="height:362px">
      <h3 class="widget-title">Recent Posts</h3>
      <svg class="flourish" width="200" height="12" viewBox="0 0 200 12"><path d="M0 6h85M115 6h85" stroke="#bbb"/><circle cx="100" cy="6" r="4" fill="none" stroke="#bbb"/></svg>
      <ul class="recent">
        <li>Lifestyles of the Tired and Wired – Module 4 of Calm Reset: Adrenal Fatigue</li>
        <li>April Essential Living Education Series</li>
        <li>Module 3: A Nice Supplement to the Program</li>
        <li>What Do You Mean I Can't Have Coffee?!? – Module 2 Calm Reset: Adrenal Fatigue</li>
        <li>DIY Emotional Regulation Blend</li>
      </ul>
    </section>

    <section class="widget" style="height:353px">
      <h3 class="widget-title">Recent Comments</h3>
      <svg class="flourish" width="200" height="12" viewBox="0 0 200 12"><path d="M0 6h85M115 6h85" stroke="#bbb"/><circle cx="100" cy="6" r="4" fill="none" stroke="#bbb"/></svg>
      <ul class="comments">
        <li><svg width="12" height="12" viewBox="0 0 12 12"><ellipse cx="6" cy="5" rx="5.5" ry="4.5" fill="none" stroke="#1f8fc0"/></svg><span>Lifestyles of the Tired and Wired – Module 4 of Calm Reset: Adrenal Fatigue <b>[...]</b></span></li>
        <li><svg width="12" height="12" viewBox="0 0 12 12"><ellipse cx="6" cy="5" rx="5.5" ry="4.5" fill="none" stroke="#1f8fc0"/></svg><span>Lifestyles of the Tired and Wired – Module 4 of Calm Reset: Adrenal Fatigue <b>[...]</b></span></li>
        <li><svg width="12" height="12" viewBox="0 0 12 12"><ellipse cx="6" cy="5" rx="5.5" ry="4.5" fill="none" stroke="#1f8fc0"/></svg><span>Lifestyles of the Tired and Wired – Module 4 of Calm Reset: Adrenal Fatigue <b>[...]</b></span></li>
      </ul>
    </section>

    <section class="widget" style="height:524px">
      <h3 class="widget-title">TR Maple Sprout on Pixly</h3>
      <svg class="flourish" width="200" height="12" viewBox="0 0 200 12"><path d="M0 6h85M115 6h85" stroke="#bbb"/><circle cx="100" cy="6" r="4" fill="none" stroke="#bbb"/></svg>
      <div class="photo-grid" role="img" aria-label="Grid of twenty-five recent social photos of food, events and friends"></div>
      <div class="insta-actions"><span class="btn-teal">Load More</span><span class="btn-green">Follow Us on Pixly</span></div>
    </section>

    <section class="widget" style="height:308px">
      <div class="promo" role="img" aria-label="Promo banner: need extra support for your 21-Day Sweet Reset, tell me more"></div>
    </section>
  </aside>
</main>

<footer class="site-footer">
  <div class="f-col">
    <h4 class="f-title">Category</h4>
    <ul class="f-list">
      <li><svg width="14" height="11" viewBox="0 0 14 11"><path d="M0 1h5l1 1.5h8V11H0z" fill="none" stroke="#fff"/></svg>21 Day Sweet Reset</li>
      <li><svg width="14" height="11" viewBox="0 0 14 11"><path d="M0 1h5l1 1.5h8V11H0z" fill="none" stroke="#fff"/></svg>Adrenal Fatigue</li>
      <li><svg width="14" height="11" viewBox="0 0 14 11"><path d="M0 1h5l1 1.5h8V11H0z" fill="none" stroke="#fff"/></svg>Articles</li>
      <li><svg width="14" height="11" viewBox="0 0 14 11"><path d="M0 1h5l1 1.5h8V11H0z" fill="none" stroke="#fff"/></svg>DIY</li>
      <li><svg width="14" height="11" viewBox="0 0 14 11"><path d="M0 1h5l1 1.5h8V11H0z" fill="none" stroke="#fff"/></svg>Essential Oils</li>
      <li><svg width="14" height="11" viewBox="0 0 14 11"><path d="M0 1h5l1 1.5h8V11H0z" fill="none" stroke="#fff"/></svg>Real Food</li>
      <li><svg width="14" height="11" viewBox="0 0 14 11"><path d="M0 1h5l1 1.5h8V11H0z" fill="none" stroke="#fff"/></svg>Uncategorized</li>
    </ul>
  </div>
  <div class="f-col">
    <h4 class="f-title">Archieves</h4>
    <ul class="f-list">
      <li><svg width="13" height="13" viewBox="0 0 13 13"><rect x="0.5" y="2" width="12" height="10.5" fill="none" stroke="#fff"/><path d="M0.5 5h12" stroke="#fff"/></svg>April 2015</li>
      <li><svg width="13" height="13" viewBox="0 0 13 13"><rect x="0.5" y="2" width="12" height="10.5" fill="none" stroke="#fff"/><path d="M0.5 5h12" stroke="#fff"/></svg>March 2015</li>
      <li><svg width="13" height="13" viewBox="0 0 13 13"><rect x="0.5" y="2" width="12" height="10.5" fill="none" stroke="#fff"/><path d="M0.5 5h12" stroke="#fff"/></svg>February 2015</li>
      <li><svg width="13" height="13" viewBox="0 0 13 13"><rect x="0.5" y="2" width="12" height="10.5" fill="none" stroke="#fff"/><path d="M0.5 5h12" stroke="#fff"/></svg>January 2015</li>
      <li><svg width="13" height="13" viewBox="0 0 13 13"><rect x="0.5" y="2" width="12" height="10.5" fill="none" stroke="#fff"/><path d="M0.5 5h12" stroke="#fff"/></svg>September 2014</li>
      <li><svg width="13" height="13" viewBox="0 0 13 13"><rect x="0.5" y="2" width="12" height="10.5" fill="none" stroke="#fff"/><path d="M0.5 5h12" stroke="#fff"/></svg>June 2014</li>
      <li><svg width="13" height="13" viewBox="0 0 13 13"><rect x="0.5" y="2" width="12" height="10.5" fill="none" stroke="#fff"/><path d="M0.5 5h12" stroke="#fff"/></svg>May 2014</li>
      <li><svg width="13" height="13" viewBox="0 0 13 13"><rect x="0.5" y="2" width="12" height="10.5" fill="none" stroke="#fff"/><path d="M0.5 5h12" stroke="#fff"/></svg>April 2014</li>
    </ul>
  </div>
  <div class="f-col">
    <h4 class="f-title">TR Maple Sprout Newsletter</h4>
    <p class="f-text">Exclusive, subscribers-only content delivered straight to your inbox</p>
    <div class="subscribe"><span>Your Email id</span><b>Submit</b></div>
    <h4 class="f-title">Follow TR Maple Sprout</h4>
    <div class="socials"><i></i><i></i><i></i><i></i></div>
  </div>
</footer>
<div class="footer-bar"><span>TR Maple Sprout</span> All Rights Reserved.</div>

</body>
</html>
```